Web Site Design

We need to design the whole web site for our small start up. We sell hospitality and culinary art internships abroad. I did my own design with WIX which is horrible meanwhile I started with my business. You can see it www.brightvoyage-intern.example I will need you to create a new and attractive web site and to leave it working on wix. The internship destinations are United Arab Emirates, Thailand, China, Spain, Brazil and maybe leave a couple of pages for future destinations.You could also get other ideas of other sites that do internships.

Target Market(s)

Students and recent graduates of hospitality and culinary art majors

Industry/Entity Type

Education

Number of Pages Required

5+ page

Requirements
Must have
• Addittional to our program destinations, or to the pages in the current site. The website must contain a page for Universities or Hotels who require our service

```html
<!DOCTYPE html>
<html lang="en">
<head>
<meta charset="utf-8">
<title>Hospitality Internships – Home</title>
<link rel="stylesheet" href="https://fonts.googleapis.com/css2?family=Abel&family=Roboto+Condensed:wght@300;400&display=swap">
<style>
:root{
  --green:#1db68f;
  --red:#b3101f;
  --ink:#222;
  --dark:#161616;
  --black:#000;
  --white:#fff;
  --muted:#555;
  --page:#ffffff;
}
*{box-sizing:border-box;margin:0;padding:0}
html,body{width:1200px;height:800px;overflow:hidden;background:var(--page)}
body{font-family:"Roboto Condensed",sans-serif;color:var(--ink);position:relative}
.site{width:1200px;height:800px;display:flex;flex-direction:column}

/* hero */
.hero{position:relative;height:230px;color:var(--white);text-align:center}
.hero-photo{position:absolute;inset:0;background:radial-gradient(ellipse at 50% 55%,#c9a45a 0%,#7a4a25 30%,#3d2a20 60%,#2b2623 100%)}
.hero-shade{position:absolute;inset:0;background:rgba(0,0,0,.35)}
.nav{position:absolute;top:0;left:0;right:0;height:46px;display:flex;align-items:center;justify-content:space-between;padding:0 60px;background:rgba(40,40,40,.55)}
.brand{font-family:"Abel",sans-serif;font-size:24px;letter-spacing:1px}
.menu{display:flex;gap:6px;list-style:none;font-family:"Abel",sans-serif;font-size:15px}
.menu li{padding:6px 12px}
.menu .active{background:var(--green)}
.hero-copy{position:absolute;top:78px;left:0;right:0}
.hero-title{font-family:"Abel",sans-serif;font-size:40px;font-weight:400}
.hero-sub{font-family:"Abel",sans-serif;font-size:18px;margin-top:2px}
.btn{display:inline-block;background:var(--red);color:var(--white);font-family:"Abel",sans-serif;border:0}
.hero .btn{margin-top:12px;font-size:19px;padding:6px 22px}

/* about */
.section-title{font-family:"Abel",sans-serif;color:var(--green);font-weight:400;font-size:22px}
.about{height:140px;display:flex;justify-content:space-between;padding:16px 100px 0 100px}
.about-text{width:560px}
.about-text p{font-size:11px;line-height:1.35;color:var(--muted);margin-top:6px}
.photo{display:block}
.about-photo{width:230px;height:115px;background:linear-gradient(135deg,#3c4a55,#8a7a66 55%,#2d3238)}

/* team */
.team{height:140px;text-align:center;padding-top:4px}
.team-grid{display:flex;justify-content:center;gap:26px;margin:8px 0 8px}
.team-photo{width:110px;height:70px}
.team-photo.p1{background:linear-gradient(135deg,#56606a,#b7a797 60%,#4a4a4e)}
.team-photo.p2{background:linear-gradient(180deg,#6b7784,#2e3542 60%,#8b3a36)}
.team-photo.p3{background:linear-gradient(135deg,#8a6a55,#2a2424 50%,#4a3a30)}
.team .btn{font-size:14px;padding:4px 16px}

/* destinations */
.destinations{position:relative;height:130px;background:linear-gradient(90deg,#2a2a2a,#3c3a38 50%,#262626);text-align:center;padding-top:8px}
.destinations .section-title{font-size:20px}
.dest-grid{display:flex;justify-content:center;gap:18px;margin-top:6px}
.dest-card{width:200px;height:84px;background:var(--white);display:flex;text-align:left}
.dest-photo{width:82px;height:84px}
.dest-photo.d1{background:linear-gradient(180deg,#c78a38,#6a4320)}
.dest-photo.d2{background:linear-gradient(180deg,#7da6c7,#a94a30)}
.dest-photo.d3{background:linear-gradient(180deg,#8fb7d8,#c28a4d)}
.dest-body{padding:6px 7px;display:flex;flex-direction:column;justify-content:space-between;align-items:flex-start}
.dest-body p{font-size:9px;line-height:1.25;color:var(--muted)}
.dest-body .btn{font-size:9px;padding:2px 8px}

/* newsletter */
.newsletter{height:82px;background:var(--green);color:var(--white);display:flex;align-items:center;justify-content:center;gap:40px}
.newsletter h2{font-family:"Abel",sans-serif;font-weight:400;font-size:22px}
.newsletter p{font-size:11px;width:300px;line-height:1.3}
.email{width:200px;height:26px;border:1px solid var(--white);background:transparent;color:var(--white);font-family:"Roboto Condensed",sans-serif;font-size:11px;padding:0 10px}
.email::placeholder{color:var(--white)}
.newsletter .btn{font-size:15px;padding:4px 14px}

/* footer */
.footer{flex:1;background:var(--black);color:var(--white);display:flex;align-items:center;justify-content:space-between;padding:0 100px;position:relative}
.footer .brand{font-size:22px}
.footer-links{display:flex;gap:24px;list-style:none;font-size:13px}
.follow{display:flex;align-items:center;gap:10px;font-size:13px}
.social{display:flex;gap:6px}
.social span{width:14px;height:14px;border:1px solid var(--white);border-radius:50%}
.legal{position:absolute;bottom:6px;left:0;right:0;text-align:center;font-size:9px;letter-spacing:1px}
</style>
</head>
<body>
<div class="site">
  <header class="hero">
    <div class="hero-photo" role="img" aria-label="Plated gourmet dish topped with shredded vegetables"></div>
    <div class="hero-shade"></div>
    <nav class="nav">
      <div class="brand">LOGO</div>
      <ul class="menu">
        <li class="active">Home</li>
        <li>About us</li>
        <li>Destination</li>
        <li>Contact</li>
      </ul>
    </nav>
    <div class="hero-copy">
      <h1 class="hero-title">Lorem Ipsum is simply</h1>
      <p class="hero-sub">Lorem Ipsum is simply dummy text of the printing</p>
      <span class="btn">Read More</span>
    </div>
  </header>

  <section class="about">
    <div class="about-text">
      <h2 class="section-title">About Us</h2>
      <p>Lorem Ipsum is simply dummy text of the printing and typesetting industry. Lorem Ipsum has been the industry's standard dummy text ever since the 1500s, when an unknown printer took a galley.</p>
      <p>Lorem Ipsum is simply dummy text of the printing and typesetting industry. Lorem Ipsum has been the industry's standard dummy text ever since the 1500s, when an unknown printer took a galley.</p>
    </div>
    <div class="photo about-photo" role="img" aria-label="Two colleagues in a meeting at a café table"></div>
  </section>

  <section class="team">
    <h2 class="section-title">Our Team</h2>
    <div class="team-grid">
      <div class="photo team-photo p1" role="img" aria-label="Team member portrait"></div>
      <div class="photo team-photo p2" role="img" aria-label="Team member in a suit on a city street"></div>
      <div class="photo team-photo p3" role="img" aria-label="Team member working at a desk"></div>
    </div>
    <span class="btn">View More</span>
  </section>

  <section class="destinations">
    <h2 class="section-title">Our Destination</h2>
    <div class="dest-grid">
      <article class="dest-card">
        <div class="dest-photo d1" role="img" aria-label="Illuminated glass pyramid at dusk"></div>
        <div class="dest-body"><p>Contrary to popular belief, Lorem Ipsum is not simply random text. It has roots in a piece of classical Latin.</p><span class="btn">Read More</span></div>
      </article>
      <article class="dest-card">
        <div class="dest-photo d2" role="img" aria-label="Traditional temple under blue sky"></div>
        <div class="dest-body"><p>Contrary to popular belief, Lorem Ipsum is not simply random text. It has roots in a piece of classical Latin.</p><span class="btn">Read More</span></div>
      </article>
      <article class="dest-card">
        <div class="dest-photo d3" role="img" aria-label="Historic plaza with canal and arches"></div>
        <div class="dest-body"><p>Contrary to popular belief, Lorem Ipsum is not simply random text. It has roots in a piece of classical Latin.</p><span class="btn">Read More</span></div>
      </article>
    </div>
  </section>

  <section class="newsletter">
    <h2>Newsletter</h2>
    <p>Contrary to popular belief, Lorem Ipsum is not simply random text. It has roots in a piece of classical Latin literature from 45 BC.</p>
    <input class="email" type="email" placeholder="Enter Your Email Adress">
    <span class="btn">Subscribe</span>
  </section>

  <footer class="footer">
    <div class="brand">LOGO</div>
    <ul class="footer-links">
      <li>Home</li>
      <li>About us</li>
      <li>Destination</li>
      <li>Contact</li>
    </ul>
    <div class="follow">Follow us
      <div class="social"><span></span><span></span><span></span></div>
    </div>
    <p class="legal">© 2016 website All Right Reserved</p>
  </footer>
</div>
</body>
</html>
```